Real Estate Business Folders, Business Cards, Envelopes & Letterhead

Im looking for trendy, modern & professional design concepts for my business folder that will be used for real estate documents and property report presentations. I'm also looking for Business card designs, envelopes and letterhead with a similar theme. I have a logo already and I would like the logo colors to be incorporated in the design concepts.

Target Market(s)

Real Estate Investors, Banks, Financial Institutions

Industry/Entity Type

Real Estate

Colors
0455a3
959595
d3d3d3
848484

Requirements
Must have
• Trendy Modern, High Class look. Please include logo and colors and incorporate some silver or metallic.
• Business Address: 4812 Corvelle Blvd ste 210-300
• Mesa Ridge, NV 89000
• Phone: 702-555-0147
• Fax : 702-555-0183
• Email: info@mesacrestlandgroup.example
• Website: MesaCrestLandGroup.example

```html
<!DOCTYPE html>
<html lang="en">
<head>
<meta charset="utf-8">
<title>Mesa Crest Land Group – Stationery Set</title>
<link href="https://fonts.googleapis.com/css2?family=Montserrat:wght@400;600;700&display=swap" rel="stylesheet">
<style>
  :root{
    --brand-blue:#0455a3;
    --brand-blue-dark:#033f7a;
    --silver:#959595;
    --silver-light:#d3d3d3;
    --silver-mid:#848484;
    --paper:#ffffff;
    --ink:#3a3a3a;
    --shadow:0 1px 4px rgba(0,0,0,.25);
  }
  *{box-sizing:border-box;margin:0;padding:0}
  html,body{width:849px;height:1200px;overflow:hidden;background:#fff}
  body{position:relative;font-family:'Montserrat',sans-serif;color:var(--ink)}
  .piece{position:absolute;background:var(--paper);box-shadow:var(--shadow);overflow:hidden}
  .piece svg.shapes{position:absolute;inset:0;width:100%;height:100%}
  .label{position:absolute;font-size:11px;font-weight:600;letter-spacing:.3px;color:#333;text-transform:uppercase}
  .brand{position:absolute;display:flex;align-items:center;gap:5px;font-weight:700;line-height:1;text-transform:uppercase}
  .brand .mark{width:9px;height:9px;background:currentColor;flex:none}
  .brand .name{font-size:11px;letter-spacing:.4px}
  .brand--light{color:#fff}
  .brand--blue{color:var(--brand-blue)}
  .contact{position:absolute;font-size:5px;line-height:8px;font-weight:400;white-space:nowrap}
  .contact--light{color:#fff}
  .contact--dark{color:var(--ink)}
  .web-band{position:absolute;font-size:5px;font-weight:600;color:var(--ink);display:flex;align-items:center;padding-left:8px;white-space:nowrap}
  .skyline{position:absolute;background:linear-gradient(180deg,rgba(255,255,255,.12),rgba(255,255,255,0))}
</style>
</head>
<body>

<!-- Business folder cover -->
<section class="piece folder-cover" style="left:51px;top:51px;width:388px;height:289px">
  <svg class="shapes" viewBox="0 0 388 289" preserveAspectRatio="none">
    <rect width="388" height="200" fill="var(--brand-blue)"/>
    <polygon points="0,210 275,92 388,150 388,289 0,289" fill="var(--paper)"/>
    <polygon points="0,190 275,78 388,136 388,156 275,100 0,214" fill="var(--silver-light)"/>
    <polygon points="0,204 275,92 388,150 388,156 275,100 0,214" fill="var(--silver)"/>
    <rect x="0" y="252" width="150" height="13" fill="var(--silver-light)"/>
  </svg>
  <div class="skyline" role="img" aria-label="Faint city skyline silhouette" style="left:150px;top:8px;width:170px;height:90px"></div>
  <div class="contact contact--light" style="left:14px;top:118px">
    702-555-0147<br>702-555-0183<br>info@mesacrestlandgroup.example<br>4812 Corvelle Blvd ste 210-300
  </div>
  <div class="web-band" style="left:0;top:252px;width:150px;height:13px">MesaCrestLandGroup.example</div>
  <div class="brand brand--blue" style="left:178px;top:212px"><span class="mark"></span><span class="name">Mesa Crest<br>Land Group</span></div>
  <div class="contact contact--dark" style="left:300px;top:212px">702-555-0147</div>
</section>
<div class="label" style="left:116px;top:354px">Business Folder Cover Front &amp; Back</div>

<!-- Letterhead -->
<section class="piece letterhead" style="left:495px;top:51px;width:326px;height:402px">
  <svg class="shapes" viewBox="0 0 326 402" preserveAspectRatio="none">
    <polygon points="0,40 240,4 326,22 326,34 240,16 0,54" fill="var(--silver-light)"/>
    <polygon points="0,50 240,14 326,30 326,34 240,16 0,54" fill="var(--silver)"/>
    <rect x="0" y="348" width="326" height="54" fill="var(--brand-blue)"/>
  </svg>
  <div class="brand brand--blue" style="left:14px;top:66px"><span class="mark"></span><span class="name">Mesa Crest<br>Land Group</span></div>
  <div class="contact contact--light" style="left:14px;top:358px">702-555-0147<br>info@mesacrestlandgroup.example</div>
  <div class="contact contact--light" style="left:175px;top:358px">702-555-0183<br>4812 Corvelle Blvd ste 210-300</div>
</section>
<div class="label" style="left:625px;top:475px">Letterhead</div>

<!-- Business folder inside -->
<section class="piece folder-inside" style="left:51px;top:396px;width:388px;height:269px">
  <svg class="shapes" viewBox="0 0 388 269" preserveAspectRatio="none">
    <polygon points="0,185 190,165 388,185 388,269 0,269" fill="var(--brand-blue)"/>
    <polygon points="0,178 190,158 388,178 388,186 190,166 0,186" fill="var(--silver-light)"/>
    <polygon points="60,200 130,180 130,200" fill="var(--silver)"/>
    <rect x="300" y="205" width="56" height="34" fill="none" stroke="var(--silver-light)" stroke-width="1"/>
  </svg>
  <div class="skyline" role="img" aria-label="Faint city skyline silhouette" style="left:20px;top:200px;width:100px;height:60px"></div>
</section>
<div class="label" style="left:150px;top:675px">Business Folder Inside</div>

<!-- Envelope -->
<section class="piece envelope" style="left:495px;top:608px;width:326px;height:156px">
  <svg class="shapes" viewBox="0 0 326 156" preserveAspectRatio="none">
    <rect x="0" y="140" width="326" height="16" fill="var(--brand-blue)"/>
    <rect x="0" y="136" width="326" height="4" fill="var(--silver-light)"/>
  </svg>
  <div class="brand brand--blue" style="left:222px;top:14px"><span class="mark"></span><span class="name">Mesa Crest<br>Land Group</span></div>
  <div class="contact contact--dark" style="left:14px;top:100px">702-555-0147<br>info@mesacrestlandgroup.example</div>
</section>
<div class="label" style="left:627px;top:795px">Envelope</div>

<!-- Insert cards -->
<section class="piece insert-front" style="left:51px;top:693px;width:189px;height:269px">
  <svg class="shapes" viewBox="0 0 189 269" preserveAspectRatio="none">
    <rect width="189" height="269" fill="var(--brand-blue)"/>
    <polygon points="0,70 95,40 189,70 189,80 95,50 0,80" fill="var(--silver-light)"/>
    <rect x="0" y="226" width="189" height="13" fill="var(--silver-light)"/>
  </svg>
  <div class="brand brand--light" style="left:40px;top:95px"><span class="mark"></span><span class="name">Mesa Crest<br>Land Group</span></div>
  <div class="web-band" style="left:0;top:226px;width:189px;height:13px">MesaCrestLandGroup.example</div>
</section>
<section class="piece insert-back" style="left:275px;top:693px;width:150px;height:269px;border:2px solid var(--brand-blue)">
  <svg class="shapes" viewBox="0 0 150 269" preserveAspectRatio="none">
    <rect x="0" y="196" width="150" height="6" fill="var(--silver-light)"/>
  </svg>
  <div class="contact contact--dark" style="left:10px;top:14px">702-555-0147<br>702-555-0183<br>info@mesacrestlandgroup.example<br>4812 Corvelle Blvd ste 210-300<br>Mesa Ridge, NV 89000</div>
  <div class="brand brand--blue" style="left:12px;top:220px"><span class="mark"></span><span class="name">Mesa Crest<br>Land Group</span></div>
</section>
<div class="label" style="left:449px;top:903px;line-height:15px">Business Folder<br>Insert Cards</div>

<!-- Business card -->
<section class="piece card-back" style="left:354px;top:1025px;width:283px;height:141px">
  <svg class="shapes" viewBox="0 0 283 141" preserveAspectRatio="none">
    <rect x="0" y="118" width="283" height="10" fill="var(--silver-light)"/>
  </svg>
  <div class="contact contact--dark" style="left:150px;top:16px">702-555-0147<br>702-555-0183<br>info@mesacrestlandgroup.example<br>4812 Corvelle Blvd ste 210-300<br>Mesa Ridge, NV 89000</div>
</section>
<section class="piece card-front" style="left:57px;top:1005px;width:283px;height:161px">
  <svg class="shapes" viewBox="0 0 283 161" preserveAspectRatio="none">
    <rect width="283" height="161" fill="var(--brand-blue)"/>
    <polygon points="150,0 283,0 283,60" fill="var(--brand-blue-dark)"/>
    <rect x="0" y="128" width="283" height="14" fill="var(--silver-light)"/>
  </svg>
  <div class="brand brand--light" style="left:22px;top:70px"><span class="mark"></span><span class="name">Mesa Crest<br>Land Group</span></div>
  <div class="web-band" style="left:0;top:128px;width:283px;height:14px">MesaCrestLandGroup.example</div>
</section>
<div class="label" style="left:666px;top:1059px;line-height:15px">Business Card<br>Front &amp; Back</div>

</body>
</html>
```